farvinta labs cybersecurity website design and development

website design and development for a cybersecurity company. we have a logo and would like site to suit logo colors and look
cybersecurity website should be secure and look professional
main example of site we want to use: https://www.plomvex.example/
site should be usable on tablet and phones

For each design proposal, please could you provide details of what language you'll use to code the website.

Target Market(s)

insurance companies, financial institutions, private SME, Africa and Europe

Coding

Coded - Design and coding required

Number of Pages Required

5+ page

Requirements
Must have
• 9 Pages:
Home
About us
Contacts
Partners
Blog
Services
( consulting, vulnerability assessment, information systems security audit, ISO compliance, Penetration testing, security awareness training, social engineering test, protection against DDoS, procurement )
Resources
Technologies
Careers
Nice to have
• nice to have all services have their own pages.
design based on logo colors and look

please provide what will be use to code the website

```html
<!DOCTYPE html>
<html lang="en">
<head>
<meta charset="utf-8">
<title>farvinta labs — mobile home and menu</title>
<link href="https://fonts.googleapis.com/css2?family=Poppins:wght@300;400;500;600;700&display=swap" rel="stylesheet">
<style>
:root{
  --navy:#0a1b3f;
  --navy-deep:#061230;
  --navy-mid:#0e2d66;
  --blue:#1a9be0;
  --blue-soft:#3d7fc4;
  --ink:#14213d;
  --grey:#7a8496;
  --line:#d5dae3;
  --page:#f3f4f7;
  --white:#ffffff;
}
*{box-sizing:border-box;margin:0;padding:0}
html,body{width:1200px;height:2420px;overflow:hidden}
body{background:var(--page);font-family:'Poppins',sans-serif;color:var(--ink);position:relative}
.side-label{position:absolute;font-weight:700;font-size:44px;color:#111;transform:rotate(-90deg);transform-origin:left top;white-space:nowrap}
.side-label.mobile{left:22px;top:290px}
.side-label.menu{left:1124px;top:250px}
.screen{position:absolute;top:40px;width:452px;height:2360px;background:var(--white);overflow:hidden;box-shadow:0 4px 22px rgba(10,27,63,.18)}
.screen.home{left:108px}
.screen.open{left:640px}
.abs{position:absolute}
.status-bar{left:0;top:0;width:100%;height:30px;background:var(--navy-deep);color:#fff;font-size:11px;font-weight:500;display:flex;align-items:center;justify-content:center}
.status-bar .sig{position:absolute;left:12px;font-size:10px;opacity:.8}
.status-bar .bat{position:absolute;right:12px;font-size:10px;opacity:.8}
.hero{left:0;top:30px;width:100%;height:310px;background:linear-gradient(160deg,var(--navy-deep),var(--navy-mid))}
.brand{display:flex;align-items:center;gap:8px;color:#fff;font-weight:600;font-size:17px}
.brand .dot{width:26px;height:26px;border-radius:50%;background:var(--blue)}
.hero .brand{left:22px;top:16px}
.burger{right:22px;top:22px;width:24px}
.burger span{display:block;height:3px;background:#fff;margin-bottom:5px;border-radius:2px}
.hero-art{left:246px;top:60px;width:206px;height:250px;background:linear-gradient(90deg,rgba(14,45,102,0),#1c5fb0 60%,#2a82d4)}
.hero-kicker{left:22px;top:104px;font-size:12px;color:#9fd5ff}
.hero-title{left:22px;top:124px;width:220px;font-size:20px;line-height:27px;font-weight:700;color:#fff}
.btn{display:inline-flex;align-items:center;justify-content:center;border-radius:20px;font-size:9px;font-weight:600;letter-spacing:.5px;height:26px}
.btn.fill{background:var(--blue);color:#fff}
.btn.ghost{border:1.5px solid #fff;color:#fff}
.hero .btn.fill{left:22px;top:210px;width:96px}
.hero .btn.ghost{left:128px;top:210px;width:96px}
.feature-art{left:96px;top:370px;width:260px;height:330px;border-radius:6px;background:linear-gradient(180deg,#2a6cc0,#0c2455)}
.about-kicker{left:40px;top:745px;font-size:10px;font-weight:600;color:var(--blue)}
.about-title{left:40px;top:762px;width:340px;font-size:19px;line-height:25px;font-weight:700;color:var(--ink)}
.about-copy{left:40px;top:822px;width:372px;font-size:9.5px;line-height:16px;color:var(--grey)}
.about .btn{left:40px;top:920px;width:104px}
.provide{left:0;top:1000px;width:100%;height:340px;background:linear-gradient(180deg,var(--navy),var(--navy-deep))}
.section-title{width:100%;text-align:center;font-size:20px;font-weight:300}
.section-title b{font-weight:700}
.provide .section-title{top:30px;color:#fff}
.provide-sub{top:64px;left:60px;width:332px;text-align:center;font-size:9.5px;line-height:15px;color:#9fb0cc}
.service-shield{left:136px;top:102px}
.service-name{left:136px;top:208px;width:180px;text-align:center;font-size:10px;line-height:14px;font-weight:600;color:#fff}
.chev{font-size:22px;color:#6f86b2}
.provide .chev.l{left:54px;top:178px}
.provide .chev.r{right:54px;top:178px}
.dots{width:100%;display:flex;justify-content:center;gap:7px}
.dots i{width:6px;height:6px;border-radius:50%;background:#5b6f96;display:block}
.dots i.on{background:#fff}
.provide .dots{top:318px}
.partners .section-title{top:1378px;color:var(--ink)}
.partner-card{top:1428px;width:168px;height:72px;background:#fff;border-radius:6px;box-shadow:0 2px 12px rgba(10,27,63,.14);display:flex;align-items:center;justify-content:center}
.partner-card.a{left:46px}
.partner-card.b{left:238px}
.partner-badge{width:96px;height:22px;border-radius:4px}
.partner-card.a .partner-badge{background:#d9342b}
.partner-card.b .partner-badge{background:#2a7bd3}
.partners .chev{color:#9aa3b4;top:1448px}
.partners .chev.l{left:18px}
.partners .chev.r{right:18px}
.blog .section-title{top:1552px;color:var(--ink)}
.blog-art{left:128px;top:1598px;width:196px;height:104px;border-radius:4px;background:linear-gradient(135deg,#0d3a86,#2fa8ff)}
.blog-meta{left:128px;top:1712px;font-size:8px;color:var(--grey)}
.blog-title{left:128px;top:1726px;width:196px;font-size:10.5px;line-height:15px;font-weight:600;color:var(--ink)}
.blog-copy{left:128px;top:1760px;width:196px;font-size:8.5px;line-height:13px;color:var(--grey)}
.blog-more{left:128px;top:1808px;font-size:9px;font-weight:600;color:var(--blue)}
.round-arrow{width:26px;height:26px;border-radius:50%;border:1.5px solid var(--blue);color:var(--blue);font-size:13px;display:flex;align-items:center;justify-content:center}
.blog .round-arrow.l{left:62px;top:1700px}
.blog .round-arrow.r{left:364px;top:1700px}
.contact-title{left:40px;top:1906px;font-size:18px;font-weight:300;color:var(--ink)}
.contact-title b{font-weight:700}
.field{width:172px;border-bottom:1px solid var(--line);height:34px;font-size:8.5px;color:var(--grey);font-weight:500}
.field.wide{width:372px}
.send{left:374px;top:2118px;width:38px;height:38px;border-radius:50%;background:var(--blue);display:flex;align-items:center;justify-content:center}
.footer{left:0;top:2170px;width:100%;height:190px}
.footer-wave{left:0;top:0}
.footer .brand{left:0;width:100%;justify-content:center;top:36px;font-size:16px}
.footer-links{left:60px;width:332px;display:flex;justify-content:space-between;font-size:8.5px;color:#b7c3da}
.footer-links.r1{top:86px}
.footer-links.r2{top:104px}
.socials{top:130px;width:100%;display:flex;justify-content:center;gap:8px}
.socials i{display:block;width:16px;height:16px;border-radius:50%;background:var(--blue)}
.copyright{top:160px;width:100%;text-align:center;font-size:7.5px;color:#7f8db0}
.menu-panel{left:0;top:30px;width:100%;height:510px;background:rgba(4,12,34,.94)}
.menu-panel .brand{left:22px;top:16px}
.menu-close{right:24px;top:14px;font-size:24px;color:#fff;font-weight:300}
.menu-list{left:40px;top:66px;width:372px;list-style:none}
.menu-list li{height:56px;border-bottom:1px solid rgba(255,255,255,.12);display:flex;align-items:center;justify-content:center;position:relative;color:#fff;font-size:13px;font-weight:500}
.menu-list li .more{position:absolute;right:6px;font-size:12px;color:#8fb6e6}
</style>
</head>
<body>
<div class="side-label mobile">Mobile</div>
<div class="side-label menu">Menu</div>

<section class="screen home">
  <div class="abs status-bar"><span class="sig">●●●●○</span>4:21 PM<span class="bat">100%</span></div>
  <header class="abs hero">
    <div class="abs hero-art" role="img" aria-label="Hero illustration: digital globe with security shield"></div>
    <div class="abs brand"><span class="dot"></span>farvinta labs</div>
    <div class="abs burger"><span></span><span></span><span></span></div>
    <p class="abs hero-kicker">Protect business from</p>
    <h1 class="abs hero-title">Cyber Threats and Digitalisation Risks</h1>
    <span class="abs btn fill">GET STARTED</span>
    <span class="abs btn ghost">LEARN MORE</span>
  </header>
  <div class="abs feature-art" role="img" aria-label="Feature artwork: server room inside a security shield"></div>
  <div class="about">
    <p class="abs about-kicker">ABOUT US</p>
    <h2 class="abs about-title">LOREM IPSUM IS SIMPLY DUMMY TEXT OF THE PRINTING</h2>
    <p class="abs about-copy">We help insurers, banks and growing businesses stay safe online. Our team audits systems, tests defences and trains staff so that every layer of your organisation is ready for modern threats. From first review to ongoing support, we stay beside you and keep your data protected.</p>
    <span class="abs btn fill">READ MORE</span>
  </div>
  <section class="abs provide">
    <h2 class="abs section-title">WHAT <b>WE PROVIDE</b></h2>
    <p class="abs provide-sub">Clear, practical security services built for finance and insurance teams.</p>
    <span class="abs chev l">‹</span><span class="abs chev r">›</span>
    <svg class="abs service-shield" width="180" height="200" viewBox="0 0 180 200">
      <defs><linearGradient id="sg1" x1="0" y1="0" x2="0" y2="1"><stop offset="0" stop-color="#1e7fd6"/><stop offset="1" stop-color="#0b2a66"/></linearGradient></defs>
      <path d="M90 4 L172 30 V96 C172 146 134 178 90 196 C46 178 8 146 8 96 V30 Z" fill="url(#sg1)" stroke="#3fb4ff" stroke-width="2"/>
      <circle cx="90" cy="68" r="24" fill="none" stroke="#fff" stroke-width="2"/>
      <circle cx="90" cy="62" r="7" fill="#fff"/>
      <path d="M77 82 C80 72 100 72 103 82" fill="#fff"/>
    </svg>
    <p class="abs service-name">VULNERABILITY<br>ASSESSMENT</p>
    <div class="abs dots"><i></i><i class="on"></i><i></i><i></i></div>
  </section>
  <section class="partners">
    <h2 class="abs section-title">OUR <b>PARTNERS</b></h2>
    <span class="abs chev l">‹</span><span class="abs chev r">›</span>
    <div class="abs partner-card a"><span class="partner-badge"></span></div>
    <div class="abs partner-card b"><span class="partner-badge"></span></div>
  </section>
  <section class="blog">
    <h2 class="abs section-title">LATEST <b>BLOG</b></h2>
    <span class="abs round-arrow l">‹</span><span class="abs round-arrow r">›</span>
    <div class="abs blog-art" role="img" aria-label="Blog photo: digital lock on circuit background"></div>
    <p class="abs blog-meta">12 March 2024</p>
    <h3 class="abs blog-title">Simple steps to guard your team against phishing</h3>
    <p class="abs blog-copy">Learn how short training sessions and clear rules cut risk across every office and device.</p>
    <p class="abs blog-more">Read more</p>
  </section>
  <section class="contact">
    <h2 class="abs contact-title">GET <b>IN TOUCH</b></h2>
    <div class="abs field" style="left:40px;top:1950px">First name</div>
    <div class="abs field" style="left:240px;top:1950px">Last name</div>
    <div class="abs field" style="left:40px;top:1994px">Email address</div>
    <div class="abs field" style="left:240px;top:1994px">Phone</div>
    <div class="abs field wide" style="top:2038px;left:40px">Message</div>
    <div class="abs send"><svg width="18" height="18" viewBox="0 0 24 24"><path d="M2 12 L22 3 L17 21 L11 14 Z" fill="#fff"/></svg></div>
  </section>
  <footer class="abs footer">
    <svg class="abs footer-wave" width="452" height="190" viewBox="0 0 452 190"><path d="M0 24 Q226 -14 452 24 V190 H0 Z" fill="#0a1b3f"/></svg>
    <div class="abs brand"><span class="dot"></span>farvinta labs</div>
    <div class="abs footer-links r1"><span>Home</span><span>About</span><span>Services</span><span>Partners</span></div>
    <div class="abs footer-links r2"><span>Blog</span><span>Resources</span><span>Careers</span><span>Contact</span></div>
    <div class="abs socials"><i></i><i></i><i></i><i></i></div>
    <p class="abs copyright">© 2024 farvinta labs. All rights reserved.</p>
  </footer>
</section>

<section class="screen open">
  <div class="abs status-bar"><span class="sig">●●●●○</span>4:21 PM<span class="bat">100%</span></div>
  <header class="abs hero">
    <div class="abs hero-art" role="img" aria-label="Hero illustration: digital globe with security shield"></div>
  </header>
  <div class="abs feature-art" role="img" aria-label="Feature artwork: server room inside a security shield"></div>
  <nav class="abs menu-panel">
    <div class="abs brand"><span class="dot"></span>farvinta labs</div>
    <span class="abs menu-close">×</span>
    <ul class="abs menu-list">
      <li>Home</li>
      <li>About</li>
      <li>Services<span class="more">›</span></li>
      <li>Partners</li>
      <li>Blog</li>
      <li>Resources<span class="more">›</span></li>
      <li>Contact Us</li>
    </ul>
  </nav>
  <div class="about">
    <p class="abs about-kicker">ABOUT US</p>
    <h2 class="abs about-title">LOREM IPSUM IS SIMPLY DUMMY TEXT OF THE PRINTING</h2>
    <p class="abs about-copy">We help insurers, banks and growing businesses stay safe online. Our team audits systems, tests defences and trains staff so that every layer of your organisation is ready for modern threats. From first review to ongoing support, we stay beside you and keep your data protected.</p>
    <span class="abs btn fill">READ MORE</span>
  </div>
  <section class="abs provide">
    <h2 class="abs section-title">WHAT <b>WE PROVIDE</b></h2>
    <p class="abs provide-sub">Clear, practical security services built for finance and insurance teams.</p>
    <span class="abs chev l">‹</span><span class="abs chev r">›</span>
    <svg class="abs service-shield" width="180" height="200" viewBox="0 0 180 200">
      <defs><linearGradient id="sg2" x1="0" y1="0" x2="0" y2="1"><stop offset="0" stop-color="#1e7fd6"/><stop offset="1" stop-color="#0b2a66"/></linearGradient></defs>
      <path d="M90 4 L172 30 V96 C172 146 134 178 90 196 C46 178 8 146 8 96 V30 Z" fill="url(#sg2)" stroke="#3fb4ff" stroke-width="2"/>
      <circle cx="90" cy="68" r="24" fill="none" stroke="#fff" stroke-width="2"/>
      <circle cx="90" cy="62" r="7" fill="#fff"/>
      <path d="M77 82 C80 72 100 72 103 82" fill="#fff"/>
    </svg>
    <p class="abs service-name">VULNERABILITY<br>ASSESSMENT</p>
    <div class="abs dots"><i></i><i class="on"></i><i></i><i></i></div>
  </section>
  <section class="partners">
    <h2 class="abs section-title">OUR <b>PARTNERS</b></h2>
    <span class="abs chev l">‹</span><span class="abs chev r">›</span>
    <div class="abs partner-card a"><span class="partner-badge"></span></div>
    <div class="abs partner-card b"><span class="partner-badge"></span></div>
  </section>
  <section class="blog">
    <h2 class="abs section-title">LATEST <b>BLOG</b></h2>
    <span class="abs round-arrow l">‹</span><span class="abs round-arrow r">›</span>
    <div class="abs blog-art" role="img" aria-label="Blog photo: digital lock on circuit background"></div>
    <p class="abs blog-meta">12 March 2024</p>
    <h3 class="abs blog-title">Simple steps to guard your team against phishing</h3>
    <p class="abs blog-copy">Learn how short training sessions and clear rules cut risk across every office and device.</p>
    <p class="abs blog-more">Read more</p>
  </section>
  <section class="contact">
    <h2 class="abs contact-title">GET <b>IN TOUCH</b></h2>
    <div class="abs field" style="left:40px;top:1950px">First name</div>
    <div class="abs field" style="left:240px;top:1950px">Last name</div>
    <div class="abs field" style="left:40px;top:1994px">Email address</div>
    <div class="abs field" style="left:240px;top:1994px">Phone</div>
    <div class="abs field wide" style="top:2038px;left:40px">Message</div>
    <div class="abs send"><svg width="18" height="18" viewBox="0 0 24 24"><path d="M2 12 L22 3 L17 21 L11 14 Z" fill="#fff"/></svg></div>
  </section>
  <footer class="abs footer">
    <svg class="abs footer-wave" width="452" height="190" viewBox="0 0 452 190"><path d="M0 24 Q226 -14 452 24 V190 H0 Z" fill="#0a1b3f"/></svg>
    <div class="abs brand"><span class="dot"></span>farvinta labs</div>
    <div class="abs footer-links r1"><span>Home</span><span>About</span><span>Services</span><span>Partners</span></div>
    <div class="abs footer-links r2"><span>Blog</span><span>Resources</span><span>Careers</span><span>Contact</span></div>
    <div class="abs socials"><i></i><i></i><i></i><i></i></div>
    <p class="abs copyright">© 2024 farvinta labs. All rights reserved.</p>
  </footer>
</section>
</body>
</html>
```